Looking for an attention grabbing company marketing brief/portfolio document for potential clients

We are looking for someone to take a number of our existing marketing documents and combine them into a new fresh design that will showcase our experience to our clients. The final design should be less than 5 pages highlighting our company experience and can be used to send to new potential clients.

Target Market(s)

Construction, Project Management, Commercial buildings, Restaurants, Retail

Industry/Entity Type

Consultant

Font styles to use
Sans Serif

Requirements
Must have
• A company overview, benefits, featured projects. Eye catching design that speaks clearly to the experience of our company and why customers should use us. Branding should match our current colour scheme and theme. Our website is brightmoorsitecrafts.com

```html
<!DOCTYPE html>
<html lang="en">
<head>
<meta charset="utf-8">
<title>Brightmoor Site Crafts – Project Services</title>
<link rel="stylesheet" href="https://fonts.googleapis.com/css2?family=Montserrat:ital,wght@0,300;0,400;0,500;0,600;0,700;1,700&family=Open+Sans:wght@700&family=PT+Sans+Narrow:wght@400&display=swap">
<style>
:root{
  --navy:#1b2f86;
  --navy-deep:#14226a;
  --ink:#1e3a6e;
  --slate:#2e4a6b;
  --orange:#f7a21b;
  --orange-light:#fdc21a;
  --orange-text:#f6a623;
  --paper:#dfe6ec;
  --white:#ffffff;
}
*{margin:0;padding:0;box-sizing:border-box}
html,body{width:927px;height:1200px;overflow:hidden;background:var(--paper)}
.sheet{position:relative;width:927px;height:1200px;overflow:hidden;
  background:linear-gradient(180deg,#e8edf1 0%,#d9e1e8 100%);
  font-family:"Montserrat",sans-serif;color:var(--ink)}
.abs{position:absolute}
.backdrop{position:absolute;left:0;top:0}
.tagline{left:80px;top:112px;font-style:italic;font-weight:700;
  font-size:24px;line-height:28px;color:var(--slate)}
.team-photo{left:18px;top:236px;width:372px;height:292px;border-radius:6px;
  background:linear-gradient(160deg,#e9d98a 0%,#c9d4df 22%,#9fb1c4 55%,#3f5378 100%)}
.headline{right:67px;top:64px;text-align:right;color:var(--white);font-weight:700;
  font-size:20px;line-height:24px;letter-spacing:.6px}
.rule{height:2px;background:#5b86d8;left:481px;width:379px}
.pitch{right:67px;top:157px;text-align:right;color:var(--orange-text);font-family:"Open Sans",sans-serif;
  font-weight:700;font-size:19.5px;line-height:30.5px}
.experience{right:67px;top:324px;text-align:right;color:var(--white);font-weight:400;
  font-size:17.3px;line-height:24.3px}
.brand{right:69px;top:468px;display:flex;align-items:center;gap:8px;color:var(--white);
  font-weight:700;font-size:21px}
.brand-dot{width:14px;height:14px;border-radius:50%;background:var(--orange)}
.benefits{left:0;top:530px;width:442px;height:490px;border-radius:0 60px 0 40px;
  background:linear-gradient(180deg,var(--orange-light) 0%,var(--orange) 100%);
  padding:37px 30px 0 58px;color:var(--white)}
.benefit h2{font-weight:700;font-size:17.5px;line-height:21px;letter-spacing:.7px;margin-bottom:18px}
.benefit p{font-family:"PT Sans Narrow",sans-serif;font-size:17.6px;line-height:20.4px;
  color:#1a1a1a;text-align:justify;width:330px}
.benefit+.benefit{margin-top:36px}
.value-title{left:480px;top:603px;font-weight:700;font-size:24px;line-height:24px;color:var(--ink);letter-spacing:.5px}
.stage{width:102px;height:102px;border-radius:50%;background:var(--white);left:502px;
  display:flex;align-items:center;justify-content:center;text-align:center;
  font-weight:700;font-size:9.5px;line-height:11px;color:#1a1a1a;
  box-shadow:3px 4px 6px rgba(0,0,0,.18)}
.stage.design{top:672px;border:3px solid var(--orange)}
.stage.manage{top:786px;border:3px solid var(--navy)}
.stage.build{top:901px;border:3px solid var(--navy-deep)}
.offer{left:666px;width:250px;color:#1a1a1a}
.offer h3{font-weight:700;font-size:16.5px;letter-spacing:.4px;margin-bottom:1px}
.offer ul{list-style:none}
.offer li{position:relative;font-weight:300;font-size:16px;line-height:17.3px;white-space:nowrap}
.offer li::before{content:"•";position:absolute;left:-20px;color:var(--orange);font-weight:700}
.offer.specialization{top:649px}
.offer.services{top:804px}
.footer{left:0;top:1020px;width:927px;height:180px;
  background:linear-gradient(180deg,var(--navy) 0%,#2a3566 100%);color:var(--white);
  font-size:17.6px;line-height:19.5px}
.col{position:absolute;top:34px}
.col h4{font-weight:700;font-size:18px;letter-spacing:.5px;line-height:20px}
.col.follow{left:55px}
.col.toronto{left:314px}
.col.saskatoon{left:559px}
.col.toronto h4,.col.saskatoon h4{color:var(--orange)}
.gap{margin-top:19px;font-weight:500}
.web{color:var(--orange);font-weight:700}
</style>
</head>
<body>
<div class="sheet">
  <svg class="backdrop" width="927" height="1200" viewBox="0 0 927 1200" aria-hidden="true">
    <circle cx="735" cy="160" r="448" fill="none" stroke="#3f7ea0" stroke-width="1.2"/>
    <circle cx="726" cy="160" r="440" fill="var(--navy)"/>
  </svg>

  <p class="abs tagline">Committed to<br>quality &amp; safety</p>

  <div class="abs team-photo" role="img" aria-label="Photo: three engineers in yellow hard hats reviewing construction plans at a table"></div>

  <h1 class="abs headline">WE COMPLETE PROJECTS ON<br>TIME &amp; WITHIN BUDGET</h1>
  <div class="abs rule" style="top:133px"></div>
  <p class="abs pitch">Is a full service project management firm<br>offering a unique business model comprised<br>of a lean, well-structured team to tackle<br>your project needs at competitive rates</p>
  <div class="abs rule" style="top:300px"></div>
  <p class="abs experience">Our management team collectively offers<br>over 30 years of experience managing<br>projects with a variety of clients in<br>commercial &amp; industrial sectors.</p>

  <div class="abs brand"><span>Brightmoor Site Crafts</span><span class="brand-dot"></span></div>

  <section class="abs benefits">
    <div class="benefit">
      <h2>STREAMLINED COMMUNICATION</h2>
      <p>We tap in to your team's core values and processes to create a well managed client relationship. Together, we will reduce the probability of design challenges.</p>
    </div>
    <div class="benefit">
      <h2>COST &amp; SCHEDULE CONTROL</h2>
      <p>For time and cost-efficient project delivery, we have our finger on the pulse ready to discover and eliminate organizational and monetary risks before they become an issue</p>
    </div>
    <div class="benefit">
      <h2>DESIGN DEVELOPMENT</h2>
      <p>From constructability reviews, cost &amp; schedule control measures, change management procedures down to audits, we strive to ensure creative, cost efficient designs are realized.</p>
    </div>
  </section>

  <h2 class="abs value-title">WHERE WE<br>ADD VALUE</h2>
  <div class="abs stage design">DESIGN<br>DEVELOPMENT</div>
  <div class="abs stage manage">PROJECT<br>MANAGEMENT</div>
  <div class="abs stage build">CONSTRUCTION<br>MANAGEMENT</div>

  <div class="abs offer specialization">
    <h3>SPECIALIZATION</h3>
    <ul>
      <li>Industrial &amp; Infrastructure<br>Development</li>
      <li>Corporate Offices, and<br>Commercial Spaces</li>
      <li>Sustainable Design &amp;<br>Green Standards</li>
      <li>Planning &amp; Design</li>
    </ul>
  </div>
  <div class="abs offer services">
    <h3>SERVICES</h3>
    <ul>
      <li>Rezoning Applications,<br>Permitting</li>
      <li>Corporate, Retail &amp;<br>Restaurant Design</li>
      <li>Concept Options &amp;<br>Maximum Best Use Design</li>
      <li>Pricing Drawings and<br>Bidding Services</li>
      <li>Construction Strategy</li>
      <li>Facilities Management</li>
    </ul>
  </div>

  <footer class="abs footer">
    <div class="col follow">
      <h4>FOLLOW US</h4>
      <p>@brightmoorsitecrafts</p>
      <p>@BMSiteCrafts</p>
    </div>
    <div class="col toronto">
      <h4>TORONTO</h4>
      <p>48 Harbourline Road</p>
      <p>Toronto, ON M5V 2K9</p>
      <p class="gap">(866) 555 0142</p>
    </div>
    <div class="col saskatoon">
      <h4>SASKATOON</h4>
      <p>115B – 1840 Prairie Way</p>
      <p>Saskatoon, SK S7K 4R2</p>
      <p class="gap">info@brightmoorsitecrafts.com</p>
      <p class="web">www.brightmoorsitecrafts.com</p>
    </div>
  </footer>
</div>
</body>
</html>
```